Company PowerPoint Presentation Template

I am looking for a business powerpoint template tailored to my company that specializes in permafrost services for the mining, transportation, and oil & gas industries. The template would be used to present project findings from studies completed for our clients. I am looking for a crisp, technical, professional business look to the template. Our business is located in North America and English is the primary language used to communicate our work. Complimentary colors associated with the business is blue (RGB, 0,112,192) or something similar in color.

```html
<!DOCTYPE html>
<html lang="en">
<head>
<meta charset="utf-8">
<title>Tundra Ground Consulting – Presentation Template Overview</title>
<link href="https://fonts.googleapis.com/css2?family=Open+Sans:wght@300;400;600;700&display=swap" rel="stylesheet">
<style>
:root{
  --blue:#0070c0;
  --blue-light:#3d9be0;
  --dark:#3a3a3c;
  --darker:#2b2b2d;
  --ink:#333336;
  --grey:#8a8a8e;
  --grey-light:#c9c9cc;
  --page:#ffffff;
}
*{box-sizing:border-box;margin:0;padding:0}
html,body{width:1200px;height:1200px;overflow:hidden;background:var(--page)}
body{font-family:'Open Sans',Arial,sans-serif;color:var(--ink)}
.deck{position:absolute;left:31px;top:50px;display:grid;grid-template-columns:repeat(5,206px);grid-auto-rows:116px;column-gap:27px;row-gap:24.6px}
.slide{position:relative;width:206px;height:116px;background:#fff;overflow:hidden;box-shadow:0 2px 6px rgba(0,0,0,.35)}
.slide.dark{background:var(--dark)}
.slide>*{position:absolute}
.panel{background:var(--dark)}
.panel.black{background:var(--darker)}
.panel.blue{background:var(--blue)}
.ph-snow{background:linear-gradient(135deg,#eef2f6 0%,#b9c4d0 55%,#7d8a98 100%)}
.ph-rock{background:linear-gradient(160deg,#e9edf1 0%,#a9b2ba 45%,#5e5a52 80%,#8a3b2a 100%)}
.ph-blue{background:radial-gradient(circle at 40% 40%,#7fd3e8 0%,#3b97d6 55%,#1f5fa8 100%)}
.ph-tundra{background:linear-gradient(180deg,#b7bcbf 0%,#6e6a58 45%,#3d3a30 100%)}
.ph-ice{background:linear-gradient(135deg,#f2f2f2 0%,#c7c7c7 50%,#8d8d8d 100%)}
.ph-aerial{background:linear-gradient(120deg,#dfe7ef 0%,#9fb0c2 40%,#5f7690 70%,#c9d3dc 100%)}
.ph-green{background:linear-gradient(135deg,#9aa58a 0%,#6f7d5d 50%,#a89f8c 100%)}
.ph-site{background:linear-gradient(170deg,#cfd6dc 0%,#6b7468 45%,#3c4236 75%,#b8532a 100%)}
.ph-desk{background:linear-gradient(135deg,#8c8a86 0%,#d7d2c8 50%,#5d5a55 100%)}
.ph-magenta{background:linear-gradient(135deg,#d86aa0 0%,#6fae6a 50%,#c8d0c4 100%)}
.ph-person{background:linear-gradient(180deg,#d9d5d0 0%,#a89c90 100%)}
.ph-round{border-radius:50%}
.logo{top:5px;font-size:3.6px;font-weight:700;letter-spacing:.5px;color:var(--ink)}
.logo.r{right:10px}.logo.l{left:10px}
.logo.w{color:#fff}
.foot{left:10px;bottom:3px;font-size:1.8px;color:var(--grey)}
.foot.w{color:#bbb}
.pg{right:8px;bottom:3px;font-size:1.8px;color:var(--grey)}
.acc{width:1.4px;background:var(--blue)}
.ttl{font-size:7.2px;line-height:1.4;font-weight:400;color:var(--ink)}
.ttl.w{color:#fff}
.ttl.c{text-align:center}
.ttl.b{font-weight:700;font-size:6.6px}
.sub{font-size:3.6px;color:var(--grey);font-weight:300}
.sub.w{color:#ddd}
.sub.i{font-style:italic}
.txt{font-size:2.2px;line-height:1.55;color:var(--grey)}
.txt.w{color:#cfcfcf}
.lbl{font-size:2.6px;font-weight:700;color:var(--ink)}
.lbl.w{color:#fff}
.num{font-size:4.4px;color:var(--ink)}
.num.w{color:#fff}
.num span{display:block;font-size:2.2px;color:var(--grey);font-style:italic}
.ico{width:7px;height:7px;border:.6px solid var(--ink);border-radius:1px}
.ico.w{border-color:#fff}
svg{display:block}
</style>
</head>
<body>
<main class="deck">

<!-- 1 cover -->
<section class="slide">
  <div class="ph-aerial" role="img" aria-label="Aerial photo of a snowy mine site" style="inset:0"></div>
  <div style="left:6px;top:6px;right:6px;bottom:6px;border:.6px solid rgba(255,255,255,.6)"></div>
  <div style="left:0;top:34px;width:206px;height:48px;background:rgba(70,80,95,.45)"></div>
  <div style="left:0;width:206px;top:40px;text-align:center;color:#fff;font-size:13px;font-weight:700;letter-spacing:2px">TUNDRA</div>
  <div style="left:0;width:206px;top:57px;text-align:center;color:#fff;font-size:3.4px;letter-spacing:2px">GROUND CONSULTING</div>
  <div style="left:0;width:206px;top:68px;text-align:center;color:#fff;font-size:6px">Expert Permafrost Services</div>
  <div style="left:0;width:206px;top:77px;text-align:center;color:#fff;font-size:2.8px">Innovative Solutions to Meet Cold Region Challenges</div>
</section>

<!-- 2 about -->
<section class="slide">
  <div class="ph-snow" role="img" aria-label="Photo of a snow-covered valley" style="left:0;top:0;width:206px;height:60px"></div>
  <div style="left:0;width:206px;top:12px;text-align:center;font-size:10px;font-weight:700;letter-spacing:1.5px;color:var(--ink)">TUNDRA</div>
  <div style="left:0;width:206px;top:26px;text-align:center;font-size:2.6px;letter-spacing:1.5px">GROUND CONSULTING</div>
  <div style="left:0;width:206px;top:36px;text-align:center;font-size:5px;font-weight:700">ABOUT</div>
  <div class="lbl" style="left:32px;top:64px">Our Services</div>
  <div class="lbl" style="left:92px;top:64px">Our Mission</div>
  <div class="lbl" style="left:154px;top:64px">Our Vision</div>
  <div class="txt" style="left:16px;top:72px;width:52px;text-align:center">We deliver focused permafrost services to mining, transport and oil &amp; gas clients.</div>
  <div class="txt" style="left:76px;top:72px;width:54px;text-align:center">Our mission is to provide quality technical service and practical solutions to frozen ground challenges.</div>
  <div class="txt" style="left:138px;top:72px;width:54px;text-align:center">We aim to be the trusted partner of choice by sharing knowledge and practical designs.</div>
  <div class="acc" style="left:10px;top:72px;height:44px"></div>
  <div class="foot">© 2024 Tundra Ground Consulting LLC · All Rights Reserved</div><div class="pg">2</div>
</section>

<!-- 3 -->
<section class="slide">
  <div class="panel" style="left:0;top:0;width:206px;height:112px"></div>
  <div class="logo l w">TUNDRA</div>
  <div class="ttl w" style="left:20px;top:22px;width:80px">Your Title Tundra Ground Consulting Title goes</div>
  <div class="sub w" style="left:20px;top:55px">The Description Here</div>
  <div class="txt w" style="left:20px;top:64px;width:90px">Lorem ipsum dolor sit amet, consectetur adipiscing elit. Donec pede justo, fringilla vel aliquet nec, vulputate eget arcu. In enim justo, rhoncus ut imperdiet a, venenatis vitae justo.</div>
  <div class="ph-rock" role="img" aria-label="Photo of a rocky mountain slope with a site camp" style="left:130px;top:14px;width:68px;height:76px"></div>
  <div style="left:0;top:112px;width:206px;height:4px;background:#fff"></div>
  <div class="foot w" style="bottom:6px">© 2024 Tundra Ground Consulting LLC · All Rights Reserved</div>
</section>

<!-- 4 -->
<section class="slide">
  <div class="panel" style="left:0;top:0;width:72px;height:116px"></div>
  <div class="ph-rock" role="img" aria-label="Photo of a snowy mountain and camp" style="left:0;top:42px;width:72px;height:64px"></div>
  <div class="logo r">TUNDRA</div>
  <div class="ttl" style="left:90px;top:18px;font-size:7px">Expert Permafrost Services</div>
  <div class="txt" style="left:96px;top:28px;font-size:2.4px">Innovative Solutions to Meet Cold Region Challenges</div>
  <div class="txt" style="left:104px;top:40px;width:84px">Lorem ipsum is simply dummy text of the printing and typesetting industry. It has been the standard dummy text ever since the 1500s, when an unknown printer took a galley of type and scrambled it to make a type specimen book. It has survived five centuries and the leap into electronic typesetting, remaining essentially unchanged. It was popularised in the 1960s with the release of sheets containing passages.</div>
  <div class="acc" style="left:194px;top:74px;height:42px"></div>
  <div class="foot w">© 2024 Tundra Ground Consulting LLC · All Rights Reserved</div>
</section>

<!-- 5 -->
<section class="slide">
  <div class="panel" style="left:150px;top:0;width:56px;height:116px"></div>
  <div class="ph-aerial" role="img" aria-label="Aerial photo of a winding road through snow" style="left:118px;top:26px;width:64px;height:78px"></div>
  <div class="logo l">TUNDRA</div>
  <div class="ttl" style="left:26px;top:26px;width:80px">Your Title Tundra Ground Consulting Title goes here</div>
  <div class="txt" style="left:26px;top:62px;width:80px">Lorem ipsum dolor sit amet, consectetur adipiscing elit. Proin sed libero in magna ultrices gravida sit amet non lorem.</div>
  <div class="num" style="left:26px;top:82px">15,000<span>Customer/Days</span></div>
  <div class="num" style="left:54px;top:82px">1,000+<span>Achievement</span></div>
  <div class="num" style="left:82px;top:82px">5,901<span>Our Branch</span></div>
  <div class="foot">© 2024 Tundra Ground Consulting LLC · All Rights Reserved</div>
</section>

<!-- 6 -->
<section class="slide">
  <div class="panel blue" style="left:42px;top:58px;width:44px;height:58px"></div>
  <div class="ph-blue" role="img" aria-label="Blue thermal map image" style="left:25px;top:26px;width:47px;height:78px"></div>
  <div class="logo r">TUNDRA</div>
  <div class="ttl" style="left:103px;top:26px;width:80px">Your Title Tundra Ground Consulting Title goes here</div>
  <div class="sub" style="left:103px;top:60px;color:var(--ink)">Type Your Vision Here</div>
  <div class="txt" style="left:103px;top:66px">Our Mission</div>
  <div class="txt" style="left:103px;top:74px;width:78px">Our core mission is to provide high quality technical services and practical solutions to solve permafrost challenges.</div>
  <div class="acc" style="left:194px;top:70px;height:46px"></div>
  <div class="foot">© 2024 Tundra Ground Consulting LLC · All Rights Reserved</div>
</section>

<!-- 7 -->
<section class="slide">
  <div class="panel" style="left:134px;top:0;width:48px;height:80px"></div>
  <div class="ph-site" role="img" aria-label="Photo of a drilling rig on snowy ground" style="left:110px;top:26px;width:60px;height:84px"></div>
  <div class="logo l">TUNDRA</div>
  <div class="ttl" style="left:26px;top:26px;width:80px">Your Title Tundra Consulting Title here</div>
  <div class="sub" style="left:26px;top:48px">The Description Here</div>
  <div class="txt" style="left:26px;top:58px;width:76px">Lorem ipsum is simply dummy text of the printing and typesetting industry. It has been the standard dummy text ever since the 1500s, when an unknown printer took a galley of type and scrambled it to make a type specimen book. It has survived not only five centuries.</div>
  <div class="acc" style="left:10px;top:60px;height:56px"></div>
  <div class="foot">© 2024 Tundra Ground Consulting LLC · All Rights Reserved</div>
</section>

<!-- 8 -->
<section class="slide">
  <div class="panel" style="left:0;top:0;width:206px;height:58px"></div>
  <div class="logo l w">TUNDRA</div>
  <div class="ttl w" style="left:26px;top:26px">Talk About Our<br>Services Here</div>
  <div class="ph-rock" role="img" aria-label="Photo of a snowy mountain with a camp below" style="left:112px;top:14px;width:74px;height:86px"></div>
  <div class="txt" style="left:26px;top:62px;width:80px">Lorem ipsum dolor sit amet, consectetur adipiscing elit. Proin sed libero in magna ultrices gravida sit amet non lorem.</div>
  <div class="num" style="left:26px;top:85px">15,000<span>Your Text Here</span></div>
  <div class="num" style="left:54px;top:85px">1,000+<span>Your Text Here</span></div>
  <div class="num" style="left:82px;top:85px">782<span>Your Text Here</span></div>
  <div class="acc" style="left:10px;top:70px;height:46px"></div>
  <div class="foot">© 2024 Tundra Ground Consulting LLC · All Rights Reserved</div>
</section>

<!-- 9 -->
<section class="slide">
  <div class="panel" style="left:0;top:58px;width:206px;height:58px"></div>
  <div class="logo l">TUNDRA</div>
  <div class="ttl" style="left:24px;top:24px">Talk About Our<br>Services Here</div>
  <div class="ph-tundra" role="img" aria-label="Photo of thawing tundra ground" style="left:104px;top:26px;width:102px;height:64px"></div>
  <div class="sub w" style="left:24px;top:62px;color:#fff">Type Your Text Here</div>
  <div class="txt w" style="left:24px;top:70px;width:72px">Lorem ipsum dolor sit amet, consectetur adipiscing elit. Proin sed libero in magna ultrices gravida sit amet non lorem. Suspendisse potenti.</div>
  <div class="foot w">© 2024 Tundra Ground Consulting LLC · All Rights Reserved</div>
</section>

<!-- 10 -->
<section class="slide">
  <div class="panel" style="left:0;top:0;width:206px;height:116px"></div>
  <div style="left:182px;top:0;width:24px;height:116px;background:#fff"></div>
  <div class="logo l w">TUNDRA</div>
  <div class="ttl w" style="left:24px;top:24px">Talk About Our<br>Services Here</div>
  <div class="lbl w" style="left:24px;top:50px">1,900 Total Projects</div>
  <div class="sub w i" style="left:24px;top:58px;font-size:2.6px">The Description Here</div>
  <div class="txt w" style="left:24px;top:64px;width:70px">Lorem ipsum dolor sit amet, consectetur adipiscing elit. Proin sed libero in magna. • Lorem ipsum dolor sit amet • Lorem ipsum dolor sit amet</div>
  <div class="ph-magenta" role="img" aria-label="False-colour satellite image" style="left:103px;top:0;width:40px;height:50px"></div>
  <div class="ph-ice" role="img" aria-label="Photo of an ice wedge face" style="left:103px;top:50px;width:40px;height:66px"></div>
  <div class="txt" style="left:150px;top:14px;width:30px;color:#ccc">Lorem ipsum dolor sit amet, consectetur adipiscing elit. Proin sed libero in magna ultrices gravida sit amet.</div>
  <div class="txt" style="left:150px;top:60px;width:30px;color:#ccc">Lorem ipsum dolor sit amet, consectetur adipiscing elit. Suspendisse potenti gravida.</div>
  <div class="txt" style="left:184px;top:20px;width:20px">Lorem ipsum dolor sit amet, consectetur elit.</div>
  <div class="foot w">© 2024 Tundra Ground Consulting LLC · All Rights Reserved</div>
</section>

<!-- 11 -->
<section class="slide dark">
  <div style="left:182px;top:0;width:24px;height:116px;background:#fff"></div>
  <div class="logo l w" style="left:14px">TUNDRA</div>
  <div class="ttl w" style="left:25px;top:26px">Talk About Our<br>Services Here</div>
  <div class="ph-snow" role="img" aria-label="Photo of a snowy ridge" style="left:118px;top:28px;width:34px;height:24px"></div>
  <div class="ph-rock" role="img" aria-label="Photo of a drill site" style="left:163px;top:28px;width:34px;height:24px"></div>
  <div class="ph-snow" role="img" aria-label="Photo of crew on a slope" style="left:118px;top:68px;width:34px;height:24px"></div>
  <div class="ph-tundra" role="img" aria-label="Photo of tundra terrain" style="left:163px;top:68px;width:34px;height:24px"></div>
  <div class="lbl w" style="left:25px;top:58px;font-weight:400">Your Service Name</div>
  <div class="lbl w" style="left:71px;top:58px;font-weight:400">Your Service Name</div>
  <div class="txt w" style="left:25px;top:64px;width:40px">Lorem ipsum dolor sit amet, consectetur elit.</div>
  <div class="txt w" style="left:71px;top:64px;width:40px">Lorem ipsum dolor sit amet, consectetur elit.</div>
  <div class="lbl w" style="left:25px;top:80px;font-weight:400">Your Service Name</div>
  <div class="lbl w" style="left:71px;top:80px;font-weight:400">Your Service Name</div>
  <div class="txt w" style="left:25px;top:86px;width:40px">Lorem ipsum dolor sit amet, consectetur elit.</div>
  <div class="txt w" style="left:71px;top:86px;width:40px">Lorem ipsum dolor sit amet, consectetur elit.</div>
  <div class="acc" style="left:10px;top:66px;height:50px"></div>
  <div class="foot w">© 2024 Tundra Ground Consulting LLC · All Rights Reserved</div>
</section>

<!-- 12 -->
<section class="slide">
  <div class="panel" style="left:0;top:0;width:206px;height:52px"></div>
  <div class="logo l w">TUNDRA</div>
  <div class="ph-person" role="img" aria-label="Portrait photo of the talent manager" style="left:14px;top:26px;width:72px;height:80px"></div>
  <div class="ttl w" style="left:100px;top:26px">Meet Our Talent<br>Manager</div>
  <div class="sub" style="left:100px;top:57px;font-size:2.8px">Daniel Marsh, PhD</div>
  <div class="txt" style="left:100px;top:63px;width:86px">Daniel is a geotechnical engineer with 18 years of experience working on arctic and subarctic projects. He specialises in permafrost and ground ice characterisation, geothermal analysis and design of foundations for infrastructure in cold regions across North America.</div>
  <div class="acc" style="left:194px;top:70px;height:46px"></div>
  <div class="foot">© 2024 Tundra Ground Consulting LLC · All Rights Reserved</div>
</section>

<!-- 13 -->
<section class="slide">
  <div class="panel" style="left:0;top:0;width:206px;height:58px"></div>
  <div class="logo r w">TUNDRA</div>
  <div class="ph-snow" role="img" aria-label="Photo of a field crew on snow" style="left:8px;top:20px;width:62px;height:44px"></div>
  <div class="ph-green" role="img" aria-label="Aerial photo of tundra lakes" style="left:72px;top:20px;width:62px;height:44px"></div>
  <div class="ph-ice" role="img" aria-label="Photo of a frozen ground exposure" style="left:136px;top:20px;width:62px;height:44px"></div>
  <div class="lbl" style="left:14px;top:81px">DANIEL MARSH, PHD</div>
  <div class="txt" style="left:14px;top:85px;font-size:2.8px">Principal Consultant</div>
  <div class="txt" style="left:72px;top:70px;width:112px">Daniel is a geotechnical engineer with 18 years of experience on arctic and subarctic projects. He specialises in permafrost and ground ice characterisation, thermal design of infrastructure and slope stability in frozen ground for mining and transport clients across North America.</div>
  <div class="acc" style="left:194px;top:70px;height:46px"></div>
  <div class="foot">© 2024 Tundra Ground Consulting LLC · All Rights Reserved</div>
</section>

<!-- 14 -->
<section class="slide">
  <div class="panel" style="left:0;top:58px;width:206px;height:58px"></div>
  <div class="logo l">TUNDRA</div>
  <div class="ttl" style="left:25px;top:26px">Talk About Our<br>Services Here</div>
  <div class="sub i" style="left:25px;top:46px;font-size:2.6px">More Description Here</div>
  <div class="txt w" style="left:25px;top:62px;width:62px">Lorem ipsum is simply dummy text of the printing and typesetting industry. It has been the standard dummy text ever since the 1500s, when an unknown printer took a galley of type to make a type specimen book.</div>
  <div class="ph-ice" role="img" aria-label="Photo of ice-rich soil" style="left:94px;top:26px;width:46px;height:64px"></div>
  <div class="ph-ice" role="img" aria-label="Photo of frost-covered vegetation" style="left:146px;top:26px;width:46px;height:64px"></div>
  <div class="txt w" style="left:100px;top:92px;font-size:2.6px">01. Insert Your Project</div>
  <div class="txt w" style="left:152px;top:92px;font-size:2.6px">02. Insert Your Project</div>
  <div class="foot w">© 2024 Tundra Ground Consulting LLC · All Rights Reserved</div>
</section>

<!-- 15 -->
<section class="slide">
  <div class="panel" style="left:0;top:0;width:78px;height:8px"></div>
  <div class="ph-ice" role="img" aria-label="Shaded relief terrain model" style="left:8px;top:8px;width:110px;height:100px"></div>
  <div class="logo r">TUNDRA</div>
  <div class="ttl" style="left:123px;top:20px">Talk About Our<br>Services Here</div>
  <div class="sub i" style="left:123px;top:40px;font-size:2.6px">More Description Here</div>
  <div class="txt" style="left:123px;top:48px;width:66px">• Lorem ipsum is simply dummy text of the printing and typesetting industry. • It has been the standard dummy text since the 1500s. • Of type and scrambled it to make a type specimen book. • Typesetting, remaining essentially unchanged.</div>
  <div class="acc" style="left:194px;top:70px;height:46px"></div>
  <div class="foot">© 2024 Tundra Ground Consulting LLC · All Rights Reserved</div>
</section>

<!-- 16 -->
<section class="slide dark">
  <div style="left:182px;top:0;width:24px;height:116px;background:#fff"></div>
  <div class="logo r w" style="right:30px">TUNDRA</div>
  <div class="ph-site ph-round" role="img" aria-label="Circular photo of an excavated slope" style="left:10px;top:12px;width:70px;height:70px"></div>
  <div class="ttl w" style="left:110px;top:18px">Talk About Our<br>Services Here</div>
  <div class="sub w" style="left:110px;top:40px;font-size:2.4px;letter-spacing:.6px">insert subtitle here</div>
  <div class="ico w" style="left:110px;top:48px"></div><div class="lbl w" style="left:120px;top:48px">The Title Here</div><div class="txt w" style="left:120px;top:52px">Donec pede justo, fringilla vel, aliquet nec.</div>
  <div class="ico w" style="left:110px;top:60px"></div><div class="lbl w" style="left:120px;top:60px">The Title Here</div><div class="txt w" style="left:120px;top:64px">Donec pede justo, fringilla vel, aliquet nec.</div>
  <div class="ico w" style="left:110px;top:72px"></div><div class="lbl w" style="left:120px;top:72px">The Title Here</div><div class="txt w" style="left:120px;top:76px">Donec pede justo, fringilla vel, aliquet nec.</div>
  <div class="ico w" style="left:110px;top:84px"></div><div class="lbl w" style="left:120px;top:84px">The Title Here</div><div class="txt w" style="left:120px;top:88px">Donec pede justo, fringilla vel, aliquet nec.</div>
  <div class="acc" style="left:194px;top:70px;height:46px"></div>
  <div class="foot w">© 2024 Tundra Ground Consulting LLC · All Rights Reserved</div>
</section>

<!-- 17 -->
<section class="slide dark">
  <div class="logo r w">TUNDRA</div>
  <div class="ph-blue ph-round" role="img" aria-label="Circular blue thermal image" style="left:26px;top:8px;width:62px;height:62px"></div>
  <div class="ttl w" style="left:108px;top:18px">Talk About Our<br>Services Here</div>
  <div class="sub w" style="left:108px;top:40px;font-size:2.4px;letter-spacing:.6px">insert subtitle here</div>
  <div class="txt w" style="left:108px;top:46px;width:80px">Lorem ipsum is simply dummy text of the printing and typesetting industry. It has been the standard dummy text ever since the 1500s, when an unknown printer took a galley.</div>
  <div class="ico w" style="left:14px;top:74px"></div><div class="lbl w" style="left:25px;top:74px">The Title Here</div><div class="txt w" style="left:25px;top:78px">Donec pede justo, fringilla vel, aliquet nec.</div>
  <div class="ico w" style="left:14px;top:86px"></div><div class="lbl w" style="left:25px;top:86px">The Title Here</div><div class="txt w" style="left:25px;top:90px">Donec pede justo, fringilla vel, aliquet nec.</div>
  <div class="ico w" style="left:100px;top:74px"></div><div class="lbl w" style="left:111px;top:74px">The Title Here</div><div class="txt w" style="left:111px;top:78px">Donec pede justo, fringilla vel, aliquet nec.</div>
  <div class="ico w" style="left:100px;top:86px"></div><div class="lbl w" style="left:111px;top:86px">The Title Here</div><div class="txt w" style="left:111px;top:90px">Donec pede justo, fringilla vel, aliquet nec.</div>
  <div class="acc" style="left:194px;top:70px;height:46px"></div>
  <div class="foot w">© 2024 Tundra Ground Consulting LLC · All Rights Reserved</div>
</section>

<!-- 18 -->
<section class="slide">
  <div class="ph-aerial" role="img" aria-label="Aerial photo of a snowy open pit" style="left:0;top:8px;width:80px;height:100px"></div>
  <div class="logo r">TUNDRA</div>
  <div class="ttl" style="left:88px;top:14px">Talk About Our<br>Services Here</div>
  <div class="sub" style="left:88px;top:36px;font-size:2.4px;letter-spacing:.6px">insert subtitle here</div>
  <div class="txt" style="left:88px;top:42px;width:100px">Lorem ipsum is simply dummy text of the printing and typesetting industry. It has been the standard dummy text ever since the 1500s, when an unknown printer took a galley of type.</div>
  <div class="ico" style="left:88px;top:66px"></div><div class="lbl" style="left:98px;top:66px">The Title Here</div><div class="txt" style="left:98px;top:70px">Donec pede justo, fringilla.</div>
  <div class="ico" style="left:141px;top:66px"></div><div class="lbl" style="left:151px;top:66px">The Title Here</div><div class="txt" style="left:151px;top:70px">Donec pede justo, fringilla.</div>
  <div class="ico" style="left:88px;top:82px"></div><div class="lbl" style="left:98px;top:82px">The Title Here</div><div class="txt" style="left:98px;top:86px">Donec pede justo, fringilla.</div>
  <div class="ico" style="left:141px;top:82px"></div><div class="lbl" style="left:151px;top:82px">The Title Here</div><div class="txt" style="left:151px;top:86px">Donec pede justo, fringilla.</div>
  <div class="acc" style="left:194px;top:70px;height:46px"></div>
  <div class="foot">© 2024 Tundra Ground Consulting LLC · All Rights Reserved</div>
</section>

<!-- 19 -->
<section class="slide">
  <div class="panel black" style="left:176px;top:0;width:30px;height:116px"></div>
  <div class="logo l">TUNDRA</div>
  <div class="ttl b" style="left:12px;top:20px;font-weight:400">RECENT PROJECTS</div>
  <div class="txt" style="left:16px;top:32px;width:100px;color:#555">• Ridge Creek Mine, Alaska – Tailings Review<br>• Birch Flats Project, Alaska – Birch Metals<br>• North Slope, Alaska – Regional Energy<br>• Lakeview Project, Alaska – Lakeview Resources<br>• Stone Mine, Yukon – Metals<br>• Coastal Ports – Terminal Studies<br>• Airport Runway – Thermal Study<br>• Silver Bay Highway – Embankment<br>• Pine Mine, Alaska – Heavy Mining<br>• Copper Gold Project – Permitting<br>• Arctic Road Project, Alaska<br>• Graystone Project, Alaska – Valley Metals<br>• Harbor Project, Greenland – Iron<br>• Thermosyphon Foundation, Yukon<br>• Permafrost Stabilisation, Alaska<br>• Ferry River Iron Ore Mine<br>• North Basin Corporation, Alaska<br>• Cedar Mine, Saskatchewan<br>• Summit Gold Project, Canada</div>
  <div class="ph-snow" role="img" aria-label="Photo of a snowy slope" style="left:128px;top:6px;width:46px;height:32px"></div>
  <div class="ph-aerial" role="img" aria-label="Photo of a frozen river" style="left:128px;top:42px;width:46px;height:32px"></div>
  <div class="ph-ice" role="img" aria-label="Photo of frosted shrubs" style="left:128px;top:78px;width:46px;height:32px"></div>
  <div class="foot">© 2024 Tundra Ground Consulting LLC · All Rights Reserved</div>
</section>

<!-- 20 -->
<section class="slide">
  <div class="ph-rock" role="img" aria-label="Photo of a snowy mountain camp" style="left:0;top:0;width:56px;height:116px"></div>
  <div class="logo r">TUNDRA</div>
  <div class="ttl b" style="left:60px;top:20px;font-weight:400">PRESENTATIONS</div>
  <div class="txt" style="left:62px;top:32px;width:130px;color:#555">• Marsh, D. and Lee, K. 2023. Thermal performance of road embankments on warm permafrost. Cold Regions Conference.<br>• Marsh, D. 2022. Monitoring ground ice in mine waste rock. Arctic Engineering Forum.<br>• Patel, R. and Marsh, D. 2021. Foundation design for northern airports. Permafrost Symposium.<br>• Marsh, D. 2020. Slope failure risk in thawing terrain. Geotechnical Society Meeting.<br>• Lee, K. 2019. Thermosyphon systems for pipeline supports. Cold Regions Engineering.<br>• Marsh, D. 2018. Ground temperature trends in the Yukon. Northern Research Week.<br>• Patel, R. 2017. Tailings dam performance in frozen ground. Mining Geotechnics.<br>• Marsh, D. 2016. Site investigation methods for ice-rich soils. Field Methods Workshop.</div>
  <div class="acc" style="left:194px;top:70px;height:46px"></div>
  <div class="foot" style="color:#eee">© 2024 Tundra Ground Consulting LLC · All Rights Reserved</div>
</section>

<!-- 21 -->
<section class="slide">
  <div class="panel" style="left:0;top:0;width:206px;height:116px"></div>
  <div style="left:184px;top:0;width:22px;height:116px;background:#fff"></div>
  <div style="left:148px;top:0;width:36px;height:20px;background:#fff"></div>
  <div class="logo l w" style="left:14px">TUNDRA</div>
  <div class="ttl w" style="left:25px;top:26px">Talk About Our<br>Services Here</div>
  <div class="sub w" style="left:25px;top:50px">The Description Here</div>
  <div class="txt w" style="left:25px;top:60px;width:76px">Lorem ipsum dolor sit amet, consectetur adipiscing elit. Proin sed libero in magna ultrices gravida. • Lorem ipsum dolor sit amet • Lorem ipsum dolor sit amet • Lorem ipsum dolor</div>
  <div class="ph-site" role="img" aria-label="Photo of a worker at a drill rig in a forest" style="left:104px;top:20px;width:102px;height:84px"></div>
  <div class="foot w">© 2024 Tundra Ground Consulting LLC · All Rights Reserved</div>
</section>

<!-- 22 -->
<section class="slide">
  <div class="panel" style="left:0;top:0;width:206px;height:60px"></div>
  <div class="logo l w" style="left:14px">TUNDRA</div>
  <div class="ttl w c" style="left:0;width:206px;top:12px">Our Recent Projects</div>
  <div class="ph-aerial" role="img" aria-label="Aerial photo of a frozen river, January" style="left:22px;top:32px;width:76px;height:40px"></div>
  <div class="ph-green" role="img" aria-label="Aerial photo of summer tundra, June" style="left:108px;top:32px;width:76px;height:40px"></div>
  <div class="sub c" style="left:22px;width:76px;top:74px;color:var(--ink)">January 2023</div>
  <div class="sub c" style="left:108px;width:76px;top:74px;color:var(--ink)">June 2023</div>
  <div class="txt c" style="left:22px;width:76px;top:79px;font-style:italic">The Description Here</div>
  <div class="txt c" style="left:108px;width:76px;top:79px;font-style:italic">The Description Here</div>
  <div class="txt c" style="left:22px;width:76px;top:85px">Lorem ipsum dolor sit amet, consectetur adipiscing elit. Proin sed libero in magna.</div>
  <div class="txt c" style="left:108px;width:76px;top:85px">Lorem ipsum dolor sit amet, consectetur adipiscing elit. Proin sed libero in magna.</div>
  <div class="acc" style="left:10px;top:70px;height:46px"></div>
  <div class="foot">© 2024 Tundra Ground Consulting LLC · All Rights Reserved</div>
</section>

<!-- 23 -->
<section class="slide">
  <div class="ph-ice" role="img" aria-label="Photo of instrument poles in snow" style="left:4px;top:12px;width:70px;height:96px"></div>
  <div class="logo r">TUNDRA</div>
  <div class="ttl" style="left:88px;top:14px">Talk About Our<br>Services Here</div>
  <div class="sub" style="left:88px;top:36px;font-size:2.4px;letter-spacing:.6px">insert subtitle here</div>
  <div class="txt" style="left:88px;top:42px;width:100px">Lorem ipsum is simply dummy text of the printing and typesetting industry. It has been the standard dummy text ever since the 1500s, when an unknown printer took a galley of type.</div>
  <div class="ico" style="left:80px;top:66px"></div><div class="lbl" style="left:90px;top:66px">The Title Here</div><div class="txt" style="left:90px;top:70px">Donec pede justo, fringilla.</div>
  <div class="ico" style="left:133px;top:66px"></div><div class="lbl" style="left:143px;top:66px">The Title Here</div><div class="txt" style="left:143px;top:70px">Donec pede justo, fringilla.</div>
  <div class="ico" style="left:80px;top:82px"></div><div class="lbl" style="left:90px;top:82px">The Title Here</div><div class="txt" style="left:90px;top:86px">Donec pede justo, fringilla.</div>
  <div class="ico" style="left:133px;top:82px"></div><div class="lbl" style="left:143px;top:82px">The Title Here</div><div class="txt" style="left:143px;top:86px">Donec pede justo, fringilla.</div>
  <div class="acc" style="left:194px;top:70px;height:46px"></div>
  <div class="foot">© 2024 Tundra Ground Consulting LLC · All Rights Reserved</div>
</section>

<!-- 24 -->
<section class="slide">
  <div class="panel" style="left:80px;top:0;width:126px;height:116px"></div>
  <div class="logo l">TUNDRA</div>
  <div class="ttl" style="left:20px;top:18px">Our Recent<br>Projects</div>
  <div class="txt" style="left:20px;top:44px;width:56px">• Ridge Creek Mine, Alaska – Tailings<br>• Birch Flats Project – Birch Metals<br>• Stone Mine, Yukon – Metals<br>• Ferry Lake Mine – Nickel Project<br>• Pine Mine, Yukon – Land Study<br>• Silver Ridge Project – Mining Co<br>• North Basin – Energy Group<br>• Cedar Project – Lakeview Resources</div>
  <div class="ph-ice" role="img" aria-label="Photo of frozen ground exposure" style="left:94px;top:26px;width:44px;height:48px"></div>
  <div class="ph-ice" role="img" aria-label="Photo of an ice cave" style="left:148px;top:26px;width:44px;height:48px"></div>
  <div class="sub w" style="left:94px;top:78px">Your Text Here</div>
  <div class="sub w" style="left:148px;top:78px">Your Text Here</div>
  <div class="txt w" style="left:94px;top:85px;width:44px">Lorem ipsum dolor sit amet, consectetur adipiscing elit.</div>
  <div class="txt w" style="left:148px;top:85px;width:44px">Lorem ipsum dolor sit amet, consectetur adipiscing elit.</div>
  <div class="acc" style="left:10px;top:70px;height:46px"></div>
  <div class="foot">© 2024 Tundra Ground Consulting LLC · All Rights Reserved</div>
</section>

<!-- 25 -->
<section class="slide">
  <div class="panel" style="left:0;top:60px;width:206px;height:56px"></div>
  <div class="ph-aerial" role="img" aria-label="Aerial photo of a snowy valley" style="left:10px;top:14px;width:44px;height:96px"></div>
  <div class="ph-aerial" role="img" aria-label="Aerial photo of a frozen river" style="left:58px;top:14px;width:44px;height:96px"></div>
  <div class="logo r">TUNDRA</div>
  <div class="ttl" style="left:116px;top:26px">Your Title Tundra<br>Consulting Title here</div>
  <div class="sub i" style="left:116px;top:48px;font-size:2.6px">More Description Here</div>
  <div class="txt w" style="left:116px;top:62px;width:78px">Lorem ipsum is simply dummy text of the printing and typesetting industry. It has been the standard dummy text ever since the 1500s, when an unknown printer took a galley of type and scrambled it to make a type specimen book. It has survived not only five centuries.</div>
  <div class="foot w">© 2024 Tundra Ground Consulting LLC · All Rights Reserved</div>
</section>

<!-- 26 -->
<section class="slide">
  <div class="panel" style="left:146px;top:12px;width:60px;height:56px"></div>
  <div class="ph-rock" role="img" aria-label="Photo of a snowy mountain and camp" style="left:104px;top:26px;width:60px;height:90px"></div>
  <div class="logo l">TUNDRA</div>
  <div class="ttl" style="left:16px;top:26px">Your Title Tundra<br>Consulting Title here</div>
  <div class="sub i" style="left:16px;top:48px;font-size:2.6px">More Description Here</div>
  <div class="txt" style="left:16px;top:56px;width:80px">Lorem ipsum is simply dummy text of the printing and typesetting industry. It has been the standard dummy text ever since the 1500s, when an unknown printer took a galley of type and scrambled it to make a type specimen book. It has survived not only five centuries but also the leap into electronic typesetting.</div>
  <div class="acc" style="left:10px;top:74px;height:42px"></div>
  <div class="foot">© 2024 Tundra Ground Consulting LLC · All Rights Reserved</div>
</section>

<!-- 27 -->
<section class="slide">
  <div class="panel" style="left:40px;top:0;width:166px;height:116px"></div>
  <div class="ph-site" role="img" aria-label="Photo of a worker operating a drill rig" style="left:0;top:14px;width:98px;height:80px"></div>
  <div class="logo r w">TUNDRA</div>
  <div class="ttl w" style="left:112px;top:24px">Your Title Tundra<br>Consulting Title here</div>
  <div class="sub w" style="left:112px;top:46px;font-size:2.6px">Type Your Text Here</div>
  <div class="txt w" style="left:112px;top:54px;width:76px">Lorem ipsum is simply dummy text of the printing and typesetting industry. It has been the standard dummy text ever since the 1500s, when an unknown printer took a galley of type and scrambled it to make a type specimen book.</div>
  <div class="acc" style="left:194px;top:70px;height:46px"></div>
  <div class="foot w">© 2024 Tundra Ground Consulting LLC · All Rights Reserved</div>
</section>

<!-- 28 -->
<section class="slide">
  <div class="panel blue" style="left:102px;top:0;width:104px;height:72px"></div>
  <div class="ph-desk" role="img" aria-label="Photo of hands writing notes at a desk" style="left:118px;top:26px;width:88px;height:90px"></div>
  <div class="logo l">TUNDRA</div>
  <div style="left:22px;top:22px;font-size:16px;line-height:1.3;font-weight:400;color:var(--ink)">Break<br>Slides</div>
  <div class="sub" style="left:22px;top:68px;color:#555">30 Minutes !</div>
  <div class="txt" style="left:22px;top:76px;font-style:italic">Time Estimation For Break</div>
  <div class="txt" style="left:22px;top:82px;width:80px">Lorem ipsum dolor sit amet, consectetur adipiscing elit. Proin sed libero in magna ultrices gravida.</div>
  <div class="acc" style="left:10px;top:66px;height:50px"></div>
  <div class="foot">© 2024 Tundra Ground Consulting LLC · All Rights Reserved</div>
</section>

<!-- 29 -->
<section class="slide">
  <div class="panel" style="left:120px;top:0;width:86px;height:56px"></div>
  <div class="ph-ice" role="img" aria-label="Shaded relief terrain model" style="left:120px;top:56px;width:86px;height:60px"></div>
  <div class="logo l">TUNDRA</div>
  <div class="ttl" style="left:18px;top:22px">The Sumbre Data<br>Chart Here</div>
  <div class="num w" style="left:128px;top:20px;font-size:3.6px">01</div>
  <div class="lbl w" style="left:138px;top:19px;font-weight:400">Your Text Here</div>
  <div class="txt w" style="left:138px;top:24px;width:58px">Lorem ipsum dolor sit amet, consectetur adipiscing elit.</div>
  <div class="num w" style="left:128px;top:38px;font-size:3.6px">02</div>
  <div class="lbl w" style="left:138px;top:37px;font-weight:400">Your Text Here</div>
  <div class="txt w" style="left:138px;top:42px;width:58px">Lorem ipsum dolor sit amet, consectetur adipiscing elit.</div>
  <svg style="left:18px;top:50px" width="100" height="56" viewBox="0 0 100 56" aria-label="Area chart">
    <g stroke="#e2e2e2" stroke-width=".3">
      <line x1="0" y1="2" x2="100" y2="2"/><line x1="0" y1="14" x2="100" y2="14"/><line x1="0" y1="26" x2="100" y2="26"/><line x1="0" y1="38" x2="100" y2="38"/><line x1="0" y1="50" x2="100" y2="50"/>
    </g>
    <path d="M4 50 L4 18 L20 22 L36 16 L52 22 L64 34 L78 26 L96 34 L96 50 Z" fill="#a9a9ab"/>
    <path d="M4 50 L4 24 L22 30 L40 20 L56 28 L68 42 L82 34 L96 46 L96 50 Z" fill="var(--dark)"/>
  </svg>
  <div class="acc" style="left:10px;top:66px;height:50px"></div>
  <div class="foot">© 2024 Tundra Ground Consulting LLC · All Rights Reserved</div>
</section>

<!-- 30 -->
<section class="slide">
  <div class="panel" style="left:118px;top:0;width:88px;height:50px"></div>
  <div class="ph-site" role="img" aria-label="Photo of a drill rig in winter" style="left:118px;top:10px;width:64px;height:96px"></div>
  <div class="logo l">TUNDRA</div>
  <div class="ttl" style="left:26px;top:22px">Tundra<br>Ground<br>Consulting</div>
  <div class="txt" style="left:26px;top:56px;width:78px">Lorem ipsum dolor sit amet, consectetur adipiscing elit. Proin sed libero in magna ultrices gravida sit amet non lorem.</div>
  <svg style="left:30px;top:72px" width="70" height="10" viewBox="0 0 70 10" aria-label="Contact icons">
    <circle cx="5" cy="5" r="4.5" fill="var(--dark)"/><circle cx="5" cy="5" r="1.8" fill="none" stroke="#fff" stroke-width=".6"/>
    <circle cx="33" cy="5" r="4.5" fill="var(--dark)"/><circle cx="33" cy="5" r="2" fill="none" stroke="#fff" stroke-width=".6"/><line x1="31" y1="5" x2="35" y2="5" stroke="#fff" stroke-width=".5"/>
    <circle cx="61" cy="5" r="4.5" fill="var(--dark)"/><path d="M59.5 3 L61 3 L61.5 4.5 L60.8 5 Q61.5 6.5 62.5 7 L63 6.3 L64.3 6.8 L64.3 8 Q60 8 59.5 3 Z" fill="#fff"/>
  </svg>
  <div class="txt" style="left:29px;top:84px">Contact Us</div>
  <div class="txt" style="left:58px;top:84px">Website</div>
  <div class="txt" style="left:85px;top:84px">Telephone</div>
  <div class="txt" style="left:28px;top:88px">24/7 Support</div>
  <div class="txt" style="left:52px;top:88px">tundra-example.com</div>
  <div class="txt" style="left:86px;top:88px">0 0 000 000</div>
  <div class="acc" style="left:10px;top:70px;height:46px"></div>
  <div class="foot">© 2024 Tundra Ground Consulting LLC · All Rights Reserved</div>
</section>

<!-- 31 thanks -->
<section class="slide">
  <div class="ph-aerial" role="img" aria-label="Aerial photo of a snowy open pit" style="left:124px;top:14px;width:72px;height:102px"></div>
  <div class="logo l">TUNDRA</div>
  <div style="left:26px;top:36px;font-size:19px;font-weight:400;color:var(--ink)">Thanks</div>
  <div class="sub" style="left:27px;top:62px">And See You Next Time</div>
  <div class="txt" style="left:27px;top:72px;width:80px">Lorem ipsum dolor sit amet, consectetur adipiscing elit. Proin sed libero in magna ultrices gravida sit amet non lorem.</div>
  <div class="acc" style="left:10px;top:70px;height:46px"></div>
  <div class="foot">© 2024 Tundra Ground Consulting LLC · All Rights Reserved</div>
</section>

<!-- 32 timeline -->
<section class="slide">
  <div class="logo r">TUNDRA</div>
  <div class="ttl c" style="left:0;width:206px;top:14px">The Infographic</div>
  <svg style="left:22px;top:30px" width="166" height="34" viewBox="0 0 166 34" aria-label="Timeline of three milestones">
    <circle cx="28" cy="11" r="9" fill="var(--dark)"/><circle cx="82" cy="11" r="9" fill="var(--dark)"/><circle cx="136" cy="11" r="9" fill="var(--blue)"/>
    <circle cx="28" cy="11" r="3" fill="none" stroke="#fff" stroke-width=".7"/><rect x="79" y="8" width="6" height="6" fill="none" stroke="#fff" stroke-width=".7"/><path d="M134 7 L134 15 L139 13" fill="none" stroke="#fff" stroke-width=".7"/>
    <path d="M0 24 H52 L56 28 L52 32 H0 Z" fill="var(--dark)"/>
    <path d="M56 24 H106 L110 28 L106 32 H56 L60 28 Z" fill="var(--dark)"/>
    <path d="M110 24 H162 L166 28 L162 32 H110 L114 28 Z" fill="var(--blue)"/>
    <text x="28" y="29.2" fill="#fff" font-size="3" text-anchor="middle" font-family="Open Sans, sans-serif">January, 2020</text>
    <text x="82" y="29.2" fill="#fff" font-size="3" text-anchor="middle" font-family="Open Sans, sans-serif">June, 2020</text>
    <text x="138" y="29.2" fill="#fff" font-size="3" text-anchor="middle" font-family="Open Sans, sans-serif">September, 2020</text>
  </svg>
  <div class="sub c" style="left:28px;width:44px;top:70px;color:#555">Insert Your Text</div>
  <div class="sub c" style="left:82px;width:44px;top:70px;color:#555">Insert Your Text</div>
  <div class="sub c" style="left:136px;width:44px;top:70px;color:#555">Insert Your Text</div>
  <div class="txt c" style="left:28px;width:44px;top:76px">Lorem ipsum dolor sit amet, consectetur adipiscing elit.</div>
  <div class="txt c" style="left:82px;width:44px;top:76px">Lorem ipsum dolor sit amet, consectetur adipiscing elit.</div>
  <div class="txt c" style="left:136px;width:44px;top:76px">Lorem ipsum dolor sit amet, consectetur adipiscing elit.</div>
  <div class="acc" style="left:10px;top:70px;height:46px"></div>
  <div class="foot">© 2024 Tundra Ground Consulting LLC · All Rights Reserved</div>
</section>

<!-- 33 diamond -->
<section class="slide">
  <div class="logo r">TUNDRA</div>
  <div class="ttl b c" style="left:0;width:206px;top:10px">Infographic Slide</div>
  <div class="txt c" style="left:0;width:206px;top:19px">insert subtitle here</div>
  <svg style="left:70px;top:28px" width="66" height="62" viewBox="0 0 66 62" aria-label="Four-part diamond diagram">
    <path d="M4 4 H30 V18 L18 30 H4 Z" fill="var(--blue)"/>
    <path d="M62 4 H36 V18 L48 30 H62 Z" fill="var(--dark)"/>
    <path d="M4 58 H30 V44 L18 32 H4 Z" fill="#7a7a7d"/>
    <path d="M62 58 H36 V44 L48 32 H62 Z" fill="#5b5b5e"/>
    <circle cx="17" cy="16" r="3" fill="none" stroke="#fff" stroke-width=".7"/>
    <rect x="46" y="13" width="6" height="5" fill="none" stroke="#fff" stroke-width=".7"/>
    <rect x="14" y="44" width="6" height="5" fill="none" stroke="#fff" stroke-width=".7"/>
    <circle cx="49" cy="45" r="2.6" fill="none" stroke="#fff" stroke-width=".7"/><line x1="51" y1="47" x2="53" y2="49" stroke="#fff" stroke-width=".7"/>
  </svg>
  <div class="lbl" style="left:44px;top:40px">The Title Here</div><div class="txt" style="left:40px;top:44px;width:28px">Donec pede justo, fringilla vel.</div>
  <div class="lbl" style="left:44px;top:68px">The Title Here</div><div class="txt" style="left:40px;top:72px;width:28px">Donec pede justo, fringilla vel.</div>
  <div class="lbl" style="left:144px;top:40px">The Title Here</div><div class="txt" style="left:144px;top:44px;width:28px">Donec pede justo, fringilla vel.</div>
  <div class="lbl" style="left:144px;top:68px">The Title Here</div><div class="txt" style="left:144px;top:72px;width:28px">Donec pede justo, fringilla vel.</div>
  <div class="acc" style="left:10px;top:70px;height:46px"></div>
  <div class="foot">© 2024 Tundra Ground Consulting LLC · All Rights Reserved</div>
</section>

<!-- 34 four cards -->
<section class="slide">
  <div class="logo r">TUNDRA</div>
  <div class="ttl b c" style="left:0;width:206px;top:10px">Infographic Slide</div>
  <div class="txt c" style="left:0;width:206px;top:19px">insert subtitle here</div>
  <svg style="left:16px;top:34px" width="176" height="34" viewBox="0 0 176 34" aria-label="Four feature cards">
    <rect x="0" y="0" width="40" height="34" rx="3" fill="var(--blue)"/>
    <rect x="45" y="0" width="40" height="34" rx="3" fill="var(--dark)"/>
    <rect x="90" y="0" width="40" height="34" rx="3" fill="var(--dark)"/>
    <rect x="135" y="0" width="40" height="34" rx="3" fill="var(--dark)"/>
    <rect x="4" y="-2" width="12" height="10" rx="2" fill="var(--blue-light)"/>
    <rect x="49" y="-2" width="12" height="10" rx="2" fill="#58585b"/>
    <rect x="94" y="-2" width="12" height="10" rx="2" fill="#58585b"/>
    <rect x="139" y="-2" width="12" height="10" rx="2" fill="#58585b"/>
    <circle cx="10" cy="3" r="2" fill="none" stroke="#fff" stroke-width=".6"/>
    <rect x="53" y="1" width="4" height="3" fill="none" stroke="#fff" stroke-width=".6"/>
    <path d="M97 1 H103 L102 4 H98 Z" fill="none" stroke="#fff" stroke-width=".6"/>
    <circle cx="145" cy="3" r="2.2" fill="none" stroke="#fff" stroke-width=".6"/>
    <g font-family="Open Sans, sans-serif" font-size="2.6" font-weight="700" fill="#fff" text-anchor="middle">
      <text x="20" y="16">The Title Here</text><text x="65" y="16">The Title Here</text><text x="110" y="16">The Title Here</text><text x="155" y="16">The Title Here</text>
    </g>
    <g font-family="Open Sans, sans-serif" font-size="2" fill="#ddd" text-anchor="middle">
      <text x="20" y="21">Donec pede justo,</text><text x="65" y="21">Donec pede justo,</text><text x="110" y="21">Donec pede justo,</text><text x="155" y="21">Donec pede justo,</text>
      <text x="20" y="24">fringilla vel nec.</text><text x="65" y="24">fringilla vel nec.</text><text x="110" y="24">fringilla vel nec.</text><text x="155" y="24">fringilla vel nec.</text>
    </g>
  </svg>
  <div class="txt c" style="left:24px;width:160px;top:76px">Lorem ipsum dolor sit amet, consectetur adipiscing elit. Proin sed libero in magna ultrices gravida sit amet non lorem. Suspendisse potenti nulla facilisi.</div>
  <div class="acc" style="left:10px;top:70px;height:46px"></div>
  <div class="foot">© 2024 Tundra Ground Consulting LLC · All Rights Reserved</div>
</section>

<!-- 35 ring -->
<section class="slide">
  <div class="logo r">TUNDRA</div>
  <div class="ttl b c" style="left:0;width:206px;top:10px">Infographic Slide</div>
  <div class="txt c" style="left:0;width:206px;top:19px">insert subtitle here</div>
  <svg style="left:74px;top:28px" width="58" height="58" viewBox="0 0 58 58" aria-label="Four-segment ring diagram">
    <g fill="none" stroke-width="14">
      <path d="M8 27 A21 21 0 0 1 27 8" stroke="var(--blue)"/>
      <path d="M31 8 A21 21 0 0 1 50 27" stroke="var(--dark)"/>
      <path d="M50 31 A21 21 0 0 1 31 50" stroke="var(--dark)"/>
      <path d="M27 50 A21 21 0 0 1 8 31" stroke="var(--dark)"/>
    </g>
    <circle cx="16" cy="17" r="2.5" fill="none" stroke="#fff" stroke-width=".7"/>
    <rect x="39" y="15" width="6" height="4" fill="none" stroke="#fff" stroke-width=".7"/>
    <path d="M38 39 H45 L44 42 H39 Z" fill="none" stroke="#fff" stroke-width=".7"/>
    <circle cx="16" cy="41" r="2.5" fill="none" stroke="#fff" stroke-width=".7"/>
  </svg>
  <div class="lbl" style="left:46px;top:38px">The Title Here</div><div class="txt" style="left:40px;top:42px;width:28px">Donec pede justo, fringilla vel.</div>
  <div class="lbl" style="left:46px;top:68px">The Title Here</div><div class="txt" style="left:40px;top:72px;width:28px">Donec pede justo, fringilla vel.</div>
  <div class="lbl" style="left:140px;top:38px">The Title Here</div><div class="txt" style="left:140px;top:42px;width:28px">Donec pede justo, fringilla vel.</div>
  <div class="lbl" style="left:140px;top:68px">The Title Here</div><div class="txt" style="left:140px;top:72px;width:28px">Donec pede justo, fringilla vel.</div>
  <div class="acc" style="left:10px;top:70px;height:46px"></div>
  <div class="foot">© 2024 Tundra Ground Consulting LLC · All Rights Reserved</div>
</section>

<!-- 36 swirl -->
<section class="slide">
  <div class="logo r">TUNDRA</div>
  <div class="ttl b c" style="left:0;width:206px;top:10px">Infographic Slide</div>
  <div class="txt c" style="left:0;width:206px;top:19px">insert subtitle here</div>
  <svg style="left:72px;top:28px" width="62" height="62" viewBox="-31 -31 62 62" aria-label="Six-blade swirl diagram">
    <g>
      <path id="blade" d="M0 -4 Q8 -22 24 -22 Q14 -14 10 -2 Z" fill="var(--dark)"/>
      <use href="#blade" transform="rotate(60)"/>
      <use href="#blade" transform="rotate(120)"/>
      <use href="#blade" transform="rotate(180)"/>
      <use href="#blade" transform="rotate(240)"/>
      <use href="#blade" transform="rotate(300)"/>
    </g>
    <path d="M0 -4 Q8 -22 24 -22 Q14 -14 10 -2 Z" transform="rotate(240)" fill="var(--blue)"/>
  </svg>
  <div class="lbl" style="left:40px;top:34px">The Title Here</div><div class="txt" style="left:36px;top:38px;width:30px">Donec pede justo, fringilla.</div>
  <div class="lbl" style="left:40px;top:52px">The Title Here</div><div class="txt" style="left:36px;top:56px;width:30px">Donec pede justo, fringilla.</div>
  <div class="lbl" style="left:40px;top:70px">The Title Here</div><div class="txt" style="left:36px;top:74px;width:30px">Donec pede justo, fringilla.</div>
  <div class="lbl" style="left:150px;top:34px">The Title Here</div><div class="txt" style="left:150px;top:38px;width:30px">Donec pede justo, fringilla.</div>
  <div class="lbl" style="left:150px;top:52px">The Title Here</div><div class="txt" style="left:150px;top:56px;width:30px">Donec pede justo, fringilla.</div>
  <div class="lbl" style="left:150px;top:70px">The Title Here</div><div class="txt" style="left:150px;top:74px;width:30px">Donec pede justo, fringilla.</div>
  <div class="acc" style="left:10px;top:70px;height:46px"></div>
  <div class="foot">© 2024 Tundra Ground Consulting LLC · All Rights Reserved</div>
</section>

<!-- 37 pills -->
<section class="slide">
  <div class="logo r">TUNDRA</div>
  <div class="ttl b c" style="left:0;width:206px;top:10px">Infographic Slide</div>
  <div class="txt c" style="left:0;width:206px;top:19px">insert subtitle here</div>
  <svg style="left:16px;top:36px" width="176" height="14" viewBox="0 0 176 14" aria-label="Four numbered steps">
    <g fill="none" stroke-width=".7">
      <rect x="1" y="1" width="40" height="12" rx="6" stroke="var(--blue)"/>
      <rect x="45" y="1" width="40" height="12" rx="6" stroke="var(--dark)"/>
      <rect x="90" y="1" width="40" height="12" rx="6" stroke="#7a7a7d"/>
      <rect x="135" y="1" width="40" height="12" rx="6" stroke="#7a7a7d"/>
    </g>
    <circle cx="28" cy="7" r="6" fill="var(--blue)"/><circle cx="72" cy="7" r="6" fill="var(--dark)"/><circle cx="117" cy="7" r="6" fill="#7a7a7d"/><circle cx="162" cy="7" r="6" fill="#5b5b5e"/>
    <path d="M16 7 H22 M20 5 L22 7 L20 9" stroke="var(--blue)" stroke-width=".6" fill="none"/>
    <g font-family="Open Sans, sans-serif" font-size="2.6" fill="#777"><text x="5" y="8">01</text><text x="49" y="8">02</text><text x="94" y="8">03</text><text x="139" y="8">04</text></g>
  </svg>
  <div class="lbl" style="left:24px;top:56px">The Title Here</div><div class="txt" style="left:20px;top:60px;width:34px">Donec pede justo, fringilla vel.</div>
  <div class="lbl" style="left:68px;top:56px">The Title Here</div><div class="txt" style="left:64px;top:60px;width:34px">Donec pede justo, fringilla vel.</div>
  <div class="lbl" style="left:113px;top:56px">The Title Here</div><div class="txt" style="left:109px;top:60px;width:34px">Donec pede justo, fringilla vel.</div>
  <div class="lbl" style="left:158px;top:56px">The Title Here</div><div class="txt" style="left:154px;top:60px;width:34px">Donec pede justo, fringilla vel.</div>
  <div class="txt c" style="left:24px;width:160px;top:78px">Lorem ipsum dolor sit amet, consectetur adipiscing elit. Proin sed libero in magna ultrices gravida sit amet non lorem.</div>
  <div class="acc" style="left:10px;top:70px;height:46px"></div>
  <div class="foot">© 2024 Tundra Ground Consulting LLC · All Rights Reserved</div>
</section>

<!-- 38 interlocking -->
<section class="slide">
  <div class="logo r">TUNDRA</div>
  <div class="ttl b c" style="left:0;width:206px;top:10px">Infographic Slide</div>
  <div class="lbl" style="left:88px;top:26px">The Title Here</div>
  <svg style="left:82px;top:38px" width="40" height="42" viewBox="0 0 40 42" aria-label="Four interlocking blocks">
    <path d="M2 6 Q2 2 6 2 H20 V12 H12 V20 H2 Z" fill="var(--dark)"/>
    <path d="M38 6 Q38 2 34 2 H20 V12 H28 V20 H38 Z" fill="var(--blue)"/>
    <path d="M2 36 Q2 40 6 40 H20 V30 H12 V20 H2 Z" fill="var(--blue)"/>
    <path d="M38 36 Q38 40 34 40 H20 V30 H28 V20 H38 Z" fill="var(--dark)"/>
    <circle cx="7" cy="11" r="2" fill="none" stroke="#fff" stroke-width=".6"/>
    <rect x="30" y="8" width="5" height="4" fill="none" stroke="#fff" stroke-width=".6"/>
    <circle cx="7" cy="31" r="2" fill="none" stroke="#fff" stroke-width=".6"/>
    <rect x="30" y="29" width="5" height="4" fill="none" stroke="#fff" stroke-width=".6"/>
  </svg>
  <div class="lbl" style="left:88px;top:82px">The Title Here</div>
  <div class="txt c" style="left:80px;width:46px;top:86px">Donec pede justo, fringilla vel.</div>
  <div class="lbl" style="left:50px;top:44px">The Title Here</div><div class="txt" style="left:46px;top:48px;width:30px">Donec pede justo, fringilla.</div>
  <div class="lbl" style="left:50px;top:64px">The Title Here</div><div class="txt" style="left:46px;top:68px;width:30px">Donec pede justo, fringilla.</div>
  <div class="lbl" style="left:130px;top:44px">The Title Here</div><div class="txt" style="left:130px;top:48px;width:30px">Donec pede justo, fringilla.</div>
  <div class="lbl" style="left:130px;top:64px">The Title Here</div><div class="txt" style="left:130px;top:68px;width:30px">Donec pede justo, fringilla.</div>
  <div class="acc" style="left:10px;top:70px;height:46px"></div>
  <div class="foot">© 2024 Tundra Ground Consulting LLC · All Rights Reserved</div>
</section>

<!-- 39 hex grid -->
<section class="slide">
  <div class="logo r">TUNDRA</div>
  <div class="ttl b c" style="left:0;width:206px;top:10px">Infographic Slide</div>
  <div class="txt c" style="left:0;width:206px;top:19px">insert subtitle here</div>
  <svg style="left:74px;top:30px" width="60" height="56" viewBox="0 0 60 56" aria-label="Four hexagon icons">
    <g fill="none" stroke-width=".6">
      <circle cx="15" cy="14" r="12.5" stroke="var(--blue)"/><circle cx="45" cy="14" r="12.5" stroke="var(--dark)"/>
      <circle cx="15" cy="42" r="12.5" stroke="var(--dark)"/><circle cx="45" cy="42" r="12.5" stroke="var(--dark)"/>
    </g>
    <polygon points="15,4 24,9 24,19 15,24 6,19 6,9" fill="var(--blue)"/>
    <polygon points="45,4 54,9 54,19 45,24 36,19 36,9" fill="var(--dark)"/>
    <polygon points="15,32 24,37 24,47 15,52 6,47 6,37" fill="var(--dark)"/>
    <polygon points="45,32 54,37 54,47 45,52 36,47 36,37" fill="var(--dark)"/>
    <circle cx="15" cy="14" r="3" fill="none" stroke="#fff" stroke-width=".7"/>
    <circle cx="45" cy="14" r="3" fill="none" stroke="#fff" stroke-width=".7"/>
    <rect x="12" y="41" width="6" height="5" fill="none" stroke="#fff" stroke-width=".7"/>
    <rect x="42" y="39" width="6" height="6" transform="rotate(45 45 42)" fill="none" stroke="#fff" stroke-width=".7"/>
  </svg>
  <div class="lbl" style="left:46px;top:38px">The Title Here</div><div class="txt" style="left:40px;top:42px;width:28px">Donec pede justo, fringilla vel.</div>
  <div class="lbl" style="left:46px;top:68px">The Title Here</div><div class="txt" style="left:40px;top:72px;width:28px">Donec pede justo, fringilla vel.</div>
  <div class="lbl" style="left:142px;top:38px">The Title Here</div><div class="txt" style="left:142px;top:42px;width:28px">Donec pede justo, fringilla vel.</div>
  <div class="lbl" style="left:142px;top:68px">The Title Here</div><div class="txt" style="left:142px;top:72px;width:28px">Donec pede justo, fringilla vel.</div>
  <div class="acc" style="left:10px;top:70px;height:46px"></div>
  <div class="foot">© 2024 Tundra Ground Consulting LLC · All Rights Reserved</div>
</section>

<!-- 40 hex row -->
<section class="slide">
  <div class="logo r">TUNDRA</div>
  <div class="ttl b c" style="left:0;width:206px;top:10px">Infographic Slide</div>
  <div class="txt c" style="left:0;width:206px;top:19px">insert subtitle here</div>
  <svg style="left:16px;top:34px" width="176" height="30" viewBox="0 0 176 30" aria-label="Four hexagon icons in a row">
    <g fill="none" stroke-width=".6">
      <circle cx="22" cy="15" r="14" stroke="var(--blue)"/><circle cx="66" cy="15" r="14" stroke="#7a7a7d"/>
      <circle cx="110" cy="15" r="14" stroke="#7a7a7d"/><circle cx="154" cy="15" r="14" stroke="var(--dark)"/>
    </g>
    <polygon points="22,4 32,9.5 32,20.5 22,26 12,20.5 12,9.5" fill="var(--blue)"/>
    <polygon points="66,4 76,9.5 76,20.5 66,26 56,20.5 56,9.5" fill="#8e8e92"/>
    <polygon points="110,4 120,9.5 120,20.5 110,26 100,20.5 100,9.5" fill="#8e8e92"/>
    <polygon points="154,4 164,9.5 164,20.5 154,26 144,20.5 144,9.5" fill="var(--dark)"/>
    <circle cx="22" cy="15" r="3.2" fill="none" stroke="#fff" stroke-width=".7"/>
    <circle cx="66" cy="15" r="3.2" fill="none" stroke="#fff" stroke-width=".7"/>
    <rect x="107" y="12" width="6" height="6" transform="rotate(45 110 15)" fill="none" stroke="#fff" stroke-width=".7"/>
    <rect x="151" y="13" width="6" height="5" fill="none" stroke="#fff" stroke-width=".7"/>
  </svg>
  <div class="lbl" style="left:30px;top:68px">The Title Here</div><div class="txt c" style="left:22px;width:32px;top:72px">Donec pede justo, fringilla vel.</div>
  <div class="lbl" style="left:74px;top:68px">The Title Here</div><div class="txt c" style="left:66px;width:32px;top:72px">Donec pede justo, fringilla vel.</div>
  <div class="lbl" style="left:118px;top:68px">The Title Here</div><div class="txt c" style="left:110px;width:32px;top:72px">Donec pede justo, fringilla vel.</div>
  <div class="lbl" style="left:162px;top:68px">The Title Here</div><div class="txt c" style="left:154px;width:32px;top:72px">Donec pede justo, fringilla vel.</div>
  <div class="acc" style="left:10px;top:70px;height:46px"></div>
  <div class="foot">© 2024 Tundra Ground Consulting LLC · All Rights Reserved</div>
</section>

</main>
</body>
</html>
```